Conflict prevention NGO needs business cards ASAP

We are a small NGO based in New Caledonia working on conflict prevention, and will be attending a OGA-sponsored conference on small arms next month. Our work involves campaigning against the proliferation of small arms in this post-conflict South Pacific island, and we need business cards to match that purpose.
Our three basic guidelines are the following:
1. We would like the logo of our organisation (see attached) included on this card. We are open to a redesign of this logo to something more stylised or abstract.
2. The card would need to be double-sided: one side in French, the other in English. The text should ideally be minimalist, uncluttered, clear and concise. We prefer the card to visually communicate our mission. As such, we would like the card to present a central image or logo, which would give us the option of printing a texture onto that image/logo later.
3. I have attached images which might inspire the designer (bullets and the famous knotted gun statue). However, these are NOT prescriptive; they are simply thematic ideas, and designers should use their own creative license. We only ask that the overall business card communicate professionalism and a seriousness of purpose, rather than sentimentalism or idealism.
Thanks to everyone who is willing to offer up a design idea! I am grateful for your time, and look forward to viewing your ideas. I apologise, but this has to be a rush job. Please get in touch if you need further guidance.
Please note that our new website will go live on Wednesday evening (Brisbane time), in case it can provide inspiration: http://www.portlumineux.org/
ENGLISH SIDE
[Name, Position] Kieran Vasko, Director
[Organisation] The Centre for a Bright Harbour
[Sub-Title] The first New Caledonian think tank
[Tel] +61407913222
[Email] centreportlumineux@postvale.net
[Website] http://www.portlumineux.org/
FRENCH SIDE
[Name, Position] Kieran Vasko, Directeur
[Organisation] Le Centre pour le Port Lumineux
[Sub-Title] Le premier pôle de réflexion calédonien
[Tel] +61407913222
*Note: We are flexible on the exact way you present the above information, and you may wish to use icons instead of "Tel." for example.

```html
<!DOCTYPE html>
<html lang="en">
<head>
<meta charset="utf-8">
<title>Kieran Vasko — Business Cards</title>
<link rel="stylesheet" href="https://fonts.googleapis.com/css2?family=Arimo:wght@400;700&family=Open+Sans:wght@400;700&display=swap">
<style>
  :root {
    --backdrop: #94714a;
    --card: #ffffff;
    --navy: #1b5a96;
    --red: #e0231c;
    --ink: #3a3a3a;
    --band-blue: #1768ab;
    --band-blue-deep: #0f4f8a;
    --band-green: #3aa53a;
    --mark: #1a63b0;
  }
  * { box-sizing: border-box; margin: 0; padding: 0; }
  html, body {
    width: 1200px;
    height: 1012px;
    overflow: hidden;
    background: var(--backdrop);
  }
  .sheet {
    position: relative;
    width: 1200px;
    height: 1012px;
  }
  .card {
    position: absolute;
    top: 89px;
    width: 467px;
    height: 818px;
    background: var(--card);
    overflow: hidden;
    box-shadow: 0 2px 6px rgba(0,0,0,0.25);
  }
  .card--en { left: 95px; }
  .card--fr { left: 609px; }

  .identity {
    position: absolute;
    top: 108px;
    left: 0;
    width: 100%;
    text-align: center;
    font-family: "Arimo", Arial, sans-serif;
  }
  .identity__name {
    font-size: 31px;
    font-weight: 700;
    color: var(--navy);
    line-height: 1.1;
  }
  .identity__role {
    font-size: 23px;
    color: var(--red);
    line-height: 1.2;
    margin-top: 2px;
  }
  .identity__org {
    font-size: 21px;
    color: var(--navy);
    line-height: 1.25;
  }

  .emblem {
    position: absolute;
    top: 238px;
    left: 0;
    width: 100%;
    height: 277px;
    display: flex;
    align-items: center;
    justify-content: center;
    gap: 14px;
    font-family: "Arimo", Arial, sans-serif;
  }
  .emblem__square {
    width: 34px;
    height: 34px;
    background: var(--mark);
  }
  .emblem__name {
    font-size: 32px;
    font-weight: 700;
    color: var(--mark);
  }

  .contact {
    position: absolute;
    top: 610px;
    left: 0;
    width: 100%;
    font-family: "Open Sans", Arial, sans-serif;
    font-size: 20px;
    color: var(--ink);
  }
  .contact__line {
    display: flex;
    align-items: center;
    justify-content: center;
    gap: 10px;
    height: 30px;
    margin-bottom: 9px;
  }
  .contact__icon {
    width: 18px;
    height: 18px;
    flex: none;
  }

  .footer-band {
    position: absolute;
    left: 0;
    bottom: 0;
    width: 100%;
    height: 128px;
  }
  .footer-band svg { display: block; width: 100%; height: 100%; }
  .footer-band__url {
    position: absolute;
    left: 0;
    bottom: 40px;
    width: 100%;
    text-align: center;
    font-family: "Open Sans", Arial, sans-serif;
    font-weight: 700;
    font-size: 20px;
    letter-spacing: 2px;
    color: #ffffff;
  }
</style>
</head>
<body>
<main class="sheet">

  <section class="card card--en" lang="en">
    <header class="identity">
      <h1 class="identity__name">Kieran Vasko</h1>
      <p class="identity__role">Director</p>
      <p class="identity__org">The Centre for a Bright Harbour</p>
    </header>

    <div class="emblem">
      <span class="emblem__square"></span>
      <span class="emblem__name">Bright Harbour</span>
    </div>

    <div class="contact">
      <p class="contact__line">
        <svg class="contact__icon" viewBox="0 0 20 20" aria-hidden="true"><circle cx="10" cy="10" r="8.5" fill="none" stroke="#1b5a96" stroke-width="1.6"/><path d="M7 5.5c-1 1-1.2 3 .6 5.4s4 3.6 5.4 3.2l.9-1.2-1.9-1.6-1 .7c-.8-.4-1.8-1.5-2.2-2.4l.7-1-1.5-2z" fill="#1b5a96"/></svg>
        +61407913222
      </p>
      <p class="contact__line">
        <svg class="contact__icon" viewBox="0 0 20 20" aria-hidden="true"><path d="M2 8l8-5 8 5v8H2z" fill="#1b5a96"/><path d="M2 8l8 5 8-5" fill="none" stroke="#fff" stroke-width="1.4"/></svg>
        centreportlumineux@postvale.net
      </p>
    </div>

    <footer class="footer-band">
      <svg viewBox="0 0 467 128" preserveAspectRatio="none" aria-hidden="true">
        <defs>
          <linearGradient id="bandEn" x1="0" y1="0" x2="0" y2="1">
            <stop offset="0" stop-color="var(--band-blue)"/>
            <stop offset="1" stop-color="var(--band-blue-deep)"/>
          </linearGradient>
        </defs>
        <path d="M0 62 Q233 -18 467 62 L467 128 L0 128 Z" fill="var(--band-green)"/>
        <path d="M0 66 Q233 -11 467 66 L467 128 L0 128 Z" fill="#ffffff"/>
        <path d="M0 74 Q233 2 467 74 L467 128 L0 128 Z" fill="url(#bandEn)"/>
      </svg>
      <p class="footer-band__url">www.portlumineux.org</p>
    </footer>
  </section>

  <section class="card card--fr" lang="fr">
    <header class="identity">
      <h1 class="identity__name">Kieran Vasko</h1>
      <p class="identity__role">Directeur</p>
      <p class="identity__org">Le Centre pour le Port Lumineux</p>
    </header>

    <div class="emblem">
      <span class="emblem__square"></span>
      <span class="emblem__name">Port Lumineux</span>
    </div>

    <div class="contact">
      <p class="contact__line">
        <svg class="contact__icon" viewBox="0 0 20 20" aria-hidden="true"><circle cx="10" cy="10" r="8.5" fill="none" stroke="#1b5a96" stroke-width="1.6"/><path d="M7 5.5c-1 1-1.2 3 .6 5.4s4 3.6 5.4 3.2l.9-1.2-1.9-1.6-1 .7c-.8-.4-1.8-1.5-2.2-2.4l.7-1-1.5-2z" fill="#1b5a96"/></svg>
        +61407913222
      </p>
      <p class="contact__line">
        <svg class="contact__icon" viewBox="0 0 20 20" aria-hidden="true"><path d="M2 8l8-5 8 5v8H2z" fill="#1b5a96"/><path d="M2 8l8 5 8-5" fill="none" stroke="#fff" stroke-width="1.4"/></svg>
        centreportlumineux@postvale.net
      </p>
    </div>

    <footer class="footer-band">
      <svg viewBox="0 0 467 128" preserveAspectRatio="none" aria-hidden="true">
        <defs>
          <linearGradient id="bandFr" x1="0" y1="0" x2="0" y2="1">
            <stop offset="0" stop-color="var(--band-blue)"/>
            <stop offset="1" stop-color="var(--band-blue-deep)"/>
          </linearGradient>
        </defs>
        <path d="M0 62 Q233 -18 467 62 L467 128 L0 128 Z" fill="var(--band-green)"/>
        <path d="M0 66 Q233 -11 467 66 L467 128 L0 128 Z" fill="#ffffff"/>
        <path d="M0 74 Q233 2 467 74 L467 128 L0 128 Z" fill="url(#bandFr)"/>
      </svg>
      <p class="footer-band__url">www.portlumineux.org</p>
    </footer>
  </section>

</main>
</body>
</html>
```